Business Card Design Project

Volleyball Club specializing in college prep training for athletes ranging in age from 5-18, for both indoor and beach volleyball.

Industry/Entity Type

Business

Contact Information for Business Card

Corinne Halvorsen
Summit VBC Club Director
corinnehalvorsen@summitvbc-demo.com
P:555-214-7730
C:555-382-1064
F:555-649-2857
Web:summitvbc-demo.com

Summit Volleyball Club Inc.
4172 Larkmoor Ave #236
Brenwick CA 90417

```html
<!DOCTYPE html>
<html lang="en">
<head>
<meta charset="utf-8">
<title>Summit VBC – Business Card</title>
<link href="https://fonts.googleapis.com/css2?family=Source+Sans+3:ital,wght@0,400;0,600;1,400&display=swap" rel="stylesheet">
<style>
  :root {
    --stage: #a7a9aa;
    --card: #eeeeef;
    --navy: #083680;
    --navy-text: #103a82;
    --white: #ffffff;
    --ring: #8a8d92;
    --accent-red: #b0343a;
  }
  * { box-sizing: border-box; margin: 0; padding: 0; }
  html, body { width: 1105px; height: 1200px; overflow: hidden; }
  body {
    background: var(--stage);
    font-family: "Source Sans 3", "Myriad Pro", sans-serif;
    position: relative;
  }
  .card {
    position: absolute;
    left: 180px;
    width: 746px;
    height: 427px;
    background: var(--card);
  }
  .card--front { top: 120px; }
  .card--back { top: 640px; }

  /* Front */
  .band {
    position: absolute;
    left: 0; right: 0;
    top: 73px; height: 278px;
    background: var(--navy);
  }
  .club-mark {
    position: absolute;
    border-radius: 50%;
    background: var(--white);
    border: 3px solid var(--ring);
    display: flex;
    align-items: center;
    justify-content: center;
    color: var(--navy-text);
    font-weight: 600;
    text-align: center;
  }
  .card--front .club-mark {
    left: 35px; top: 67px;
    width: 290px; height: 290px;
    font-size: 38px;
  }
  .contact {
    position: absolute;
    left: 374px; top: 88px;
    right: 8px;
    color: var(--white);
  }
  .contact__name { font-size: 26px; font-weight: 600; line-height: 34px; }
  .contact__title { font-size: 20px; line-height: 28px; margin-bottom: 10px; }
  .contact__address { font-size: 19px; line-height: 27px; margin-bottom: 8px; }
  .contact__list { list-style: none; font-size: 19px; line-height: 28px; }
  .contact__list li { display: flex; align-items: center; gap: 10px; white-space: nowrap; }
  .contact__list svg { width: 18px; height: 18px; fill: var(--white); flex: none; }

  /* Back */
  .card--back .club-mark {
    left: 269px; top: 74px;
    width: 208px; height: 208px;
    font-size: 28px;
  }
  .social {
    position: absolute;
    left: 0; right: 0; top: 320px;
    display: flex;
    justify-content: center;
    align-items: center;
    gap: 6px;
  }
  .social__rule {
    width: 110px; height: 1px;
    background: var(--accent-red);
    margin: 0 8px;
  }
  .social__dot {
    width: 27px; height: 27px;
    border-radius: 50%;
    border: 2px solid var(--navy-text);
    background: var(--white);
  }
  .web {
    position: absolute;
    left: 0; right: 0; top: 360px;
    text-align: center;
    color: var(--navy-text);
    font-size: 20px;
    font-style: italic;
    letter-spacing: 2.5px;
  }
</style>
</head>
<body>
  <section class="card card--front">
    <div class="band"></div>
    <div class="club-mark">Summit VBC</div>
    <div class="contact">
      <p class="contact__name">Corinne Halvorsen</p>
      <p class="contact__title">Summit VBC Club Director</p>
      <p class="contact__address">4172 Larkmoor Ave #236<br>Brenwick CA 90417</p>
      <ul class="contact__list">
        <li>
          <svg viewBox="0 0 24 24" aria-hidden="true"><path d="M6.6 10.8a15.1 15.1 0 0 0 6.6 6.6l2.2-2.2a1 1 0 0 1 1-.25 11.4 11.4 0 0 0 3.6.57 1 1 0 0 1 1 1V20a1 1 0 0 1-1 1A17 17 0 0 1 3 4a1 1 0 0 1 1-1h3.5a1 1 0 0 1 1 1c0 1.250.2 2.450.57 3.57a1 1 0 0 1-.25 1z"/></svg>
          555-214-7730
        </li>
        <li>
          <svg viewBox="0 0 24 24" aria-hidden="true"><path d="M7 1h10a2 2 0 0 1 2 2v18a2 2 0 0 1-2 2H7a2 2 0 0 1-2-2V3a2 2 0 0 1 2-2zm0 3v14h10V4zm5 15.5a1.2 1.2 0 1 0 0 2.4 1.2 1.2 0 0 0 0-2.4z"/></svg>
          555-382-1064
        </li>
        <li>
          <svg viewBox="0 0 24 24" aria-hidden="true"><path d="M7 2h8l3 3v4H7zM4 10h16a2 2 0 0 1 2 2v8a1 1 0 0 1-1 1H3a1 1 0 0 1-1-1v-8a2 2 0 0 1 2-2zm2 3v2h4v-2zm0 3v2h4v-2z"/></svg>
          555-649-2857
        </li>
        <li>
          <svg viewBox="0 0 24 24" aria-hidden="true"><path d="M2 5h20v14H2zm2 2v.5l8 5.5 8-5.5V7zm0 2.9V17h16V9.9l-8 5.5z"/></svg>
          corinnehalvorsen@summitvbc-demo.com
        </li>
      </ul>
    </div>
  </section>

  <section class="card card--back">
    <div class="club-mark">Summit VBC</div>
    <div class="social">
      <span class="social__rule"></span>
      <span class="social__dot"></span>
      <span class="social__dot"></span>
      <span class="social__dot"></span>
      <span class="social__dot"></span>
      <span class="social__rule"></span>
    </div>
    <p class="web">www.summitvbc-demo.com</p>
  </section>
</body>
</html>
```